Chiropractic healthcare group business card

We are a Portland Oregon based chiropractic healthcare group. Looking for a new business card design. Something cutting edge, that shows off our new logo and tag line.Use either of the attached logos.Our tag line = "Who would you be without pain?"I'm open to about anything, impress me!!
Target Market(s)
Chiropractic patients - Auto injury, back pain, sports injuries, neck , shoulder, hip, knee, ankle pain.
Industry/Entity Type
Chiropractic
Contact Information for Business Card
Dr. Bram Holtvick, D.C.
Clinic name - Fernway Chiropractic
2 clinics
location #1
20418 NW Marwick Road
Suite B
North Plains, OR 97133
Location #2
13529 SE Calloway Street
Portland OR 97236
Main phone line 971.555.0143
website : www.FernwayClinics.example
Tag line "Who would you be without pain?"
Colors
Designer to choose colors to be used in the design.
Requirements
Must have
- Use the logo colors -- Want the orange color to be a TRUE orange.
- Both clinic address
- phone number
- website
- personal email - b.holtvick@ReliefBeginsHere.example
- tag line - "Who would you be without pain?"

```html
<!DOCTYPE html>
<html lang="en">
<head>
<meta charset="utf-8">
<title>Fernway Chiropractic – Business Card</title>
<link rel="stylesheet" href="https://fonts.googleapis.com/css2?family=Montserrat:wght@400;500;700&family=Open+Sans:wght@700;800&display=swap">
<style>
  :root {
    --orange: #f7941d;
    --ink: #111111;
    --slate: #58595b;
    --text-grey: #4d4d4d;
    --paper: #ffffff;
    --backdrop: #d9dadc;
  }
  * { box-sizing: border-box; margin: 0; padding: 0; }
  html, body { width: 1200px; height: 1000px; overflow: hidden; }
  body {
    background: var(--backdrop);
    font-family: "Montserrat", sans-serif;
    color: var(--text-grey);
    position: relative;
  }
  .card {
    position: absolute;
    left: 250px;
    width: 700px;
    height: 400px;
    background: var(--paper);
    border-radius: 22px;
    overflow: hidden;
    box-shadow: 0 8px 24px rgba(0,0,0,0.18);
  }
  .card--front { top: 60px; }
  .card--back { top: 540px; }
  .card__wave { position: absolute; inset: 0; width: 100%; height: 100%; }

  .brand {
    position: absolute;
    display: flex;
    align-items: center;
    gap: 12px;
    z-index: 1;
  }
  .brand__dot {
    width: 22px; height: 22px;
    border-radius: 50%;
    background: var(--orange);
    flex: none;
  }
  .brand__name {
    font-family: "Montserrat", sans-serif;
    font-weight: 700;
    color: var(--ink);
    letter-spacing: 0.12em;
    text-transform: uppercase;
    line-height: 1.15;
  }
  .card--front .brand { left: 190px; top: 110px; }
  .card--front .brand__name { font-size: 30px; }
  .tagline {
    position: absolute;
    left: 205px; top: 200px;
    font-size: 17px;
    letter-spacing: 0.06em;
    color: var(--text-grey);
  }

  .contact { position: absolute; left: 58px; top: 34px; z-index: 1; }
  .contact__name {
    font-family: "Open Sans", sans-serif;
    font-weight: 800;
    font-size: 23px;
    line-height: 1.25;
    color: var(--orange);
  }
  .contact__role { font-size: 17px; line-height: 1.3; }
  .contact__rule {
    width: 18px; height: 4px;
    background: var(--orange);
    margin: 6px 0 8px;
  }
  .contact__address { font-size: 13.5px; line-height: 1.4; }
  .contact__list { list-style: none; margin-top: 2px; }
  .contact__item {
    display: flex; align-items: center; gap: 12px;
    font-size: 14.5px; line-height: 1.75;
  }
  .contact__icon { width: 15px; height: 15px; fill: var(--orange); flex: none; }
  .contact__highlight { color: var(--orange); }

  .card--back .brand { right: 48px; bottom: 78px; }
  .card--back .brand__name { font-size: 22px; text-align: right; }
</style>
</head>
<body>

<section class="card card--front" aria-label="Card front">
  <svg class="card__wave" viewBox="0 0 700 400" preserveAspectRatio="none" aria-hidden="true">
    <path d="M0,228 C150,232 280,300 420,352 C520,388 620,396 700,384 L700,400 L0,400 Z" fill="var(--orange)"/>
    <path d="M0,224 C150,228 280,296 420,348 C520,384 620,392 700,380" fill="none" stroke="var(--slate)" stroke-width="5"/>
    <path d="M60,222 C180,236 290,292 420,342 C520,378 620,386 700,376" fill="none" stroke="var(--ink)" stroke-width="3"/>
  </svg>
  <div class="brand">
    <span class="brand__dot"></span>
    <span class="brand__name">Fernway<br>Chiropractic</span>
  </div>
  <p class="tagline">Who would you be without pain?</p>
</section>

<section class="card card--back" aria-label="Card back">
  <svg class="card__wave" viewBox="0 0 700 400" preserveAspectRatio="none" aria-hidden="true">
    <path d="M0,318 C150,352 320,366 480,368 C580,369 650,358 700,342 L700,400 L0,400 Z" fill="var(--orange)"/>
    <path d="M0,313 C150,347 320,361 480,363 C580,364 650,353 700,337" fill="none" stroke="var(--slate)" stroke-width="5"/>
    <path d="M10,306 C160,340 320,354 480,357 C580,358 650,347 700,331" fill="none" stroke="var(--ink)" stroke-width="3"/>
  </svg>

  <div class="contact">
    <h1 class="contact__name">Dr. Bram Holtvick, D.C.</h1>
    <p class="contact__role">Doctor</p>
    <div class="contact__rule"></div>
    <p class="contact__address">20418 NW Marwick Road Suite B<br>North Plains, OR 97133</p>
    <div class="contact__rule"></div>
    <p class="contact__address">13529 SE Calloway Street Portland<br>OR 97236</p>
    <div class="contact__rule"></div>
    <ul class="contact__list">
      <li class="contact__item">
        <svg class="contact__icon" viewBox="0 0 24 24" aria-hidden="true"><path d="M6.6 10.8a15.1 15.1 0 0 0 6.6 6.6l2.2-2.2a1 1 0 0 1 1-.25 11.4 11.4 0 0 0 3.6.57 1 1 0 0 1 1 1V20a1 1 0 0 1-1 1A17 17 0 0 1 3 4a1 1 0 0 1 1-1h3.5a1 1 0 0 1 1 1c0 1.25.2 2.45.57 3.57a1 1 0 0 1-.25 1z"/></svg>
        <span>971.555.0143</span>
      </li>
      <li class="contact__item">
        <svg class="contact__icon" viewBox="0 0 24 24" aria-hidden="true"><path d="M2 5h20v2l-10 6L2 7z M2 9l10 6 10-6v10H2z"/></svg>
        <span>b.holtvick@ReliefBeginsHere.example</span>
      </li>
      <li class="contact__item">
        <svg class="contact__icon" viewBox="0 0 24 24" aria-hidden="true"><path d="M12 2a10 10 0 1 0 0 20 10 10 0 0 0 0-20zm0 2c1 0 2.4 2 3 5H9c.6-3 2-5 3-5zM4.3 11H8.8a17 17 0 0 0 0 2H4.3a8 8 0 0 1 0-2zm6.5 0h2.4a15 15 0 0 1 0 2h-2.4a15 15 0 0 1 0-2zm4.4 0h4.5a8 8 0 0 1 0 2h-4.5a17 17 0 0 0 0-2zM9 15h6c-.6 3-2 5-3 5s-2.4-2-3-5z"/></svg>
        <span>www.<span class="contact__highlight">FernwayClinics</span>.example</span>
      </li>
    </ul>
  </div>

  <div class="brand">
    <span class="brand__dot"></span>
    <span class="brand__name">Fernway<br>Chiropractic</span>
  </div>
</section>

</body>
</html>
```